Looking for a cool, modern Cannabis Jar Label

I want you to come up with a better, modern look for a label.

I need it sized to 4” x 3” - I plan to print directly to label printer.

I want you to use Photoshop and deliver me a layered PSD file that I can edit and modify the information as needed..

The label information will need to include places for:
(1) Strain Name - most important part of label - larger font size than rest - example Marlow Frost, KTV #7, Copperleaf Haze
(2) Pricing - for Gram, 1/8, 1/4, 1/2. and Ounce
(3) Strain Designation (Hybrid, Indica or Sativa) - maybe color coded, different color for Indica v. Sativa, just an idea
(4) THC and CBD percentages - for example 23% THC and 0.05% CBD
(5) Farm name - a place where we can add the name/logo of the business that produced the product. example - Bramwell Farms

I have attached a simple mockup showing the information.

I have also attached a few samples of labels we like to give you an idea of the look and feel we are going for.

I am wanting a very clean, modern, classy, readable look.The font will use is Gotham Font.

HI Everyone! Thank you for all of your designs. I am requesting an extension because I need more time to give adequate feedback to the designers. Thank you for your participation and all of your efforts! I will be making a decision soon!

• Gotham Font

Designer to choose colors to be used in the design.

• Thank you for your designs. I am sorry i have been slow in providing feedback, things have been really busy around here!
• I wanted to give some group general feedback. After reviewing all of the designs, there is a common theme among all of the designs that I would like to see changed.
• I would like to see the per gram pricing more prominent on the label. This is what most people are looking for when they are purchasing the product. So I would like to see this stand out from the other pricing tiers. As I think about it, they don't all need to be grouped together in a line. You could have the Per Gram pricing front and center some where and then the other pricing tiers grouped together somewhere else on the label.
• This is the order of importance of items on the label. Items at the the top of the list should be bigger than those below it.
• 1. Strain name
• 2. Pricing - being per gram the most important of all prices
• 3. THC/CBD percentages
• 4. Strain Type (indica, sativa, hybrid)
• 5. Farm name/logo
• When laying out these labels, they will be going on rounded jars and they will be on display. Think of jars with fancy labels in a candy store. They need to be eye catchy, appealing, but easy read.
• Thank you for all of your hard work, everyone is doing a great job.
• Best,
• Nadia

```html
<!DOCTYPE html>
<html lang="en">
<head>
<meta charset="utf-8">
<title>Copperleaf Haze – Jar Label</title>
<link rel="stylesheet" href="https://fonts.googleapis.com/css2?family=Montserrat:wght@300;400;700;800&display=swap">
<style>
  :root {
    --page: #ffffff;
    --ink: #000000;
    --frame: #b5b5b5;
    --tier-quarter: #7ff3fb;
    --tier-eighth: #2fd4f6;
    --tier-gram: #00b4b4;
    --tier-half: #00a1c9;
    --tier-ounce: #0089d6;
    --strain-type: #ff6a00;
    --thc: #808080;
    --cbd: #b3b3b3;
  }
  * { box-sizing: border-box; margin: 0; padding: 0; }
  html, body {
    width: 1200px; height: 849px; overflow: hidden;
    background: var(--page);
    font-family: "Montserrat", sans-serif;
    color: var(--ink);
  }
  .canvas { position: relative; width: 1200px; height: 849px; }
  .label {
    position: absolute; left: 395px; top: 270px;
    width: 410px; height: 309px;
    border: 1px solid var(--frame);
    background: var(--page);
  }
  .strain-name {
    position: absolute; left: 0; top: 22px; width: 100%;
    text-align: center; font-weight: 800; font-size: 36px;
    line-height: 36px; letter-spacing: 0.5px;
  }
  .dividers { position: absolute; left: 0; top: 0; }
  .price {
    position: absolute; border-radius: 50%;
    display: flex; flex-direction: column; align-items: center; justify-content: center;
    text-align: center;
  }
  .price .unit { font-weight: 300; font-size: 15px; line-height: 15px; }
  .price .amount { font-weight: 800; font-size: 17px; line-height: 18px; }
  .price--small { width: 58px; height: 58px; }
  .price--gram { width: 78px; height: 78px; }
  .price--gram .unit { font-size: 20px; line-height: 18px; margin-bottom: 4px; }
  .price--gram .amount { font-size: 23px; line-height: 24px; }
  .price--quarter { left: 31px; top: 120px; background: var(--tier-quarter); }
  .price--eighth { left: 101px; top: 120px; background: var(--tier-eighth); }
  .price--gram { left: 166px; top: 110px; background: var(--tier-gram); }
  .price--half { left: 252px; top: 120px; background: var(--tier-half); }
  .price--ounce { left: 321px; top: 120px; background: var(--tier-ounce); }
  .strain-type {
    position: absolute; left: 59px; top: 203px; width: 140px;
    text-align: center; color: var(--strain-type);
    font-weight: 800; font-size: 19px; letter-spacing: 0.5px;
  }
  .potency {
    position: absolute; top: 225px; width: 62px; height: 62px; border-radius: 50%;
    display: flex; flex-direction: column; align-items: center; justify-content: center;
  }
  .potency .value { font-weight: 800; font-size: 14px; line-height: 16px; }
  .potency .name { font-weight: 300; font-size: 15px; line-height: 16px; }
  .potency--thc { left: 55px; background: var(--thc); }
  .potency--cbd { left: 143px; background: var(--cbd); }
  .farm {
    position: absolute; left: 265px; top: 227px;
    display: flex; align-items: center; gap: 6px;
  }
  .farm-mark { width: 30px; height: 30px; border: 1.5px solid var(--ink); border-radius: 50%; }
  .farm-name { font-weight: 800; font-size: 11px; line-height: 12px; letter-spacing: 0.5px; }
</style>
</head>
<body>
<main class="canvas">
  <section class="label">
    <h1 class="strain-name">COPPERLEAF<br>HAZE</h1>

    <svg class="dividers" width="410" height="309" aria-hidden="true">
      <g stroke="#000" stroke-width="3" stroke-linecap="round" stroke-dasharray="0 12.4" fill="none">
        <line x1="37" y1="104" x2="373" y2="104"/>
        <line x1="37" y1="195" x2="373" y2="195"/>
        <line x1="236" y1="205" x2="236" y2="283"/>
      </g>
    </svg>

    <div class="price price--small price--quarter"><span class="unit">1/4</span><span class="amount">00$</span></div>
    <div class="price price--small price--eighth"><span class="unit">1/8</span><span class="amount">00$</span></div>
    <div class="price price--gram"><span class="unit">g</span><span class="amount">00$</span></div>
    <div class="price price--small price--half"><span class="unit">1/2</span><span class="amount">00$</span></div>
    <div class="price price--small price--ounce"><span class="unit">Ounce</span><span class="amount">00$</span></div>

    <p class="strain-type">HYBRID</p>
    <div class="potency potency--thc"><span class="value">23%</span><span class="name">THC</span></div>
    <div class="potency potency--cbd"><span class="value">0.05%</span><span class="name">CBD</span></div>

    <div class="farm">
      <span class="farm-mark"></span>
      <span class="farm-name">BRAMWELL<br>FARMS</span>
    </div>
  </section>
</main>
</body>
</html>
```